Dodgeball League website

I require a nice, cool and attractive website for a new dodgeball league competition. I will need in PSD:

- Home Page
- Generic pages for news, about us etc
- Rank page with a table of team scores. stats etc

*Please design this with a Joomla*

I have attached:
- a logo
- site map for the links
- page layout guide

Example site for layout
http://www.velomarchcircuit.com/

Design
Retro,cool feel, matches well with logo

Contact me if you have any questions
Updates

Reason: Would like to see a few more designs

Target Market(s)

Young adults 18 - 35.

Industry/Entity Type

News

Colors

Designer to choose colors to be used in the design.

Requirements
Must have
• I want a cool, retro feel to the website. Not to picky on the colors. Something that will match nicely with the logo given. I will give feedback on it.
Calm colors not too bright and overwhelming
Nice to have
• Include some pictures within the picture slider so I can get a feel for the website.
Nice clean background
Should not have
• To much clutter of text
Do not put pictures in the background.

```html
<!DOCTYPE html>
<html lang="en">
<head>
<meta charset="utf-8">
<title>Redline Throw Club</title>
<link href="https://fonts.googleapis.com/css2?family=PT+Sans:wght@400;700&family=Arimo:wght@400;700&display=swap" rel="stylesheet">
<style>
:root{
  --paper:#f4eddc;
  --paper-dark:#ebe1c9;
  --panel:#f8f2e2;
  --line:#e0d3b4;
  --red:#c9411b;
  --red-dark:#a8300f;
  --red-light:#e0622f;
  --yellow:#f2b716;
  --text:#3a2a1c;
  --muted:#5d4b3a;
  --olive:#6b4e07;
}
*{box-sizing:border-box;margin:0;padding:0}
html,body{width:779px;height:1200px;overflow:hidden}
body{background:var(--paper);font-family:"Arimo",Arial,sans-serif;color:var(--text);position:relative}
.abs{position:absolute}
h2,.title{font-family:"PT Sans",Arial,sans-serif}

.brand{left:86px;top:14px;width:110px;height:84px;display:flex;flex-direction:column;align-items:center;justify-content:center;gap:4px}
.brand .dot{width:34px;height:34px;border-radius:50%;background:var(--yellow)}
.brand span{font-family:"PT Sans",sans-serif;font-weight:700;font-size:14px;color:var(--red);text-align:center;line-height:1.05}

.results{left:222px;top:30px;width:470px;height:92px;background:#efd9a0;border-radius:4px;border:1px solid #e0c27a}
.results-tab{left:404px;top:8px;width:106px;height:21px;background:var(--yellow);border-radius:8px 8px 0 0;font-family:"PT Sans",sans-serif;font-weight:700;font-size:14px;color:var(--red-dark);text-align:center;line-height:22px}
.match{top:36px;width:110px;height:66px;background:#fff;border:1px solid #d3c6a6;border-radius:3px;text-align:center;padding-top:5px}
.match b{display:block;font-family:"PT Sans",sans-serif;font-size:10px;color:#222}
.match small{display:block;font-size:7.5px;color:#333;margin-top:2px}
.match .teams{position:absolute;left:0;right:0;top:38px;font-size:6px;line-height:7px;color:#333}
.match i{position:absolute;top:36px;width:20px;height:22px;border-radius:4px 4px 10px 10px}
.match i.a{left:6px;background:#7a4a2a}
.match i.b{right:6px;background:#2d5aa0}
.next{left:655px;top:107px;width:34px;height:11px;background:#8a6a1a;border-radius:2px;color:#fff;font-size:7px;font-weight:700;line-height:11px;text-align:center}

.nav{left:0;top:130px;width:779px;height:24px;background:linear-gradient(#dc5522,#b33512)}
.nav ul{position:absolute;left:86px;top:0;list-style:none;display:flex;height:24px}
.nav li{font-family:"PT Sans",sans-serif;font-weight:700;font-size:9.5px;color:#fff;line-height:24px;text-align:center;border-right:1px solid #a02c0c}
.nav li.on{background:var(--yellow)}

.hero{left:86px;top:164px;width:608px;height:261px;background:linear-gradient(160deg,#5b5b55 0%,#8d8a82 40%,#3f7c9c 75%,#2d6b8c 100%)}
.hero-cap{left:86px;top:401px;width:608px;height:24px;background:rgba(40,40,40,.85)}
.hero-cap h1{position:absolute;left:12px;top:3px;font-family:"Arimo",sans-serif;font-weight:700;font-size:16px;color:#fff}
.dots{position:absolute;right:12px;top:8px;display:flex;gap:5px}
.dots i{width:9px;height:9px;border-radius:50%;background:#fff}
.dots i.on{background:var(--red)}

.panel{background:var(--panel);border:1px solid var(--line);border-radius:2px}
.panel h2{position:absolute;left:5px;top:5px;font-size:14.5px;color:var(--red-dark);font-weight:700}
.news{left:86px;top:450px;width:401px;height:139px}
.news .photo{position:absolute;left:5px;top:32px;width:82px;height:98px;background:linear-gradient(#6f7a7a,#9a9a88)}
.news .lead{position:absolute;left:92px;top:32px;width:122px;font-size:7px;line-height:12px;color:var(--muted)}
.news .lead b{color:var(--red-dark);font-size:7.5px}
.news .lead em{font-style:normal;color:#222;font-weight:700;display:block}
.news ul{position:absolute;left:228px;top:34px;list-style:none}
.news li{font-size:7.5px;height:21.3px;font-weight:700}
.news li span{color:var(--red-dark);margin-left:6px}

.like{left:499px;top:450px;width:195px;height:66px;background:linear-gradient(#4a6db3,#2c4f96)}
.like p{position:absolute;left:10px;color:#fff;font-family:"PT Sans",sans-serif}
.like .sq{position:absolute;right:8px;top:7px;width:30px;height:50px;background:#fff;border-radius:3px}
.register{left:499px;top:522px;width:195px;height:67px}
.register h3{position:absolute;left:6px;top:7px;font-size:8.5px;color:var(--red-dark);font-family:"Arimo",sans-serif}
.register p{position:absolute;left:6px;top:20px;font-size:7px;color:var(--muted)}
.register .btn{position:absolute;left:4px;top:41px;width:109px;height:20px;background:var(--red);border-radius:4px;color:#fff;font-weight:700;font-size:10px;line-height:20px;padding-left:7px}
.register .btn::after{content:"";position:absolute;right:8px;top:5px;width:10px;height:10px;border-radius:50%;background:#fff}
.register .mini{position:absolute;right:6px;top:6px;width:56px;height:56px;display:flex;align-items:center;justify-content:center;text-align:center;font-family:"PT Sans",sans-serif;font-weight:700;font-size:8px;color:var(--red);line-height:1.05}

.standing{left:86px;top:606px;width:401px;height:276px}
.tabs{position:absolute;left:6px;top:28px;display:flex}
.tabs div{font-family:"PT Sans",sans-serif;font-weight:700;font-size:11.5px;color:var(--red-dark);padding:6px 7px;height:25px}
.tabs .on{background:#efd9a0;border-radius:3px 3px 0 0;color:#5b3a08}
.table-wrap{position:absolute;left:6px;top:53px;width:385px;height:216px;background:#efd9a0;padding:10px 9px}
table{width:100%;border-collapse:collapse;background:#fbf5e6;border:1px solid #e2b8a2;font-size:7.5px}
th{background:linear-gradient(var(--red-light),var(--red-dark));color:#fff;font-weight:700;height:17px;text-align:left;padding-left:10px}
td{height:18.4px;border-bottom:1px dashed #e2d6bc;font-weight:700;padding-left:10px}
td.c,th.c{text-align:center;padding-left:0}
td+td,th+th{border-left:1px solid #e2d6bc}
.up{display:inline-block;width:0;height:0;border:4px solid transparent;border-bottom:5px solid #2a9a2a;border-top:0;margin-left:5px}
.dn{display:inline-block;width:0;height:0;border:4px solid transparent;border-top:5px solid #d32;border-bottom:0;margin-left:3px}

.fbw{left:499px;top:606px;width:195px;height:120px;background:#fff;border:1px solid #c9d3e6}
.fbw .hd{height:25px;background:linear-gradient(#5b7bc0,#3a5ca3);color:#fff;font-family:"PT Sans",sans-serif;font-weight:700;font-size:13px;padding:3px 5px}
.fbw .arr{position:absolute;top:8px;width:11px;height:11px;background:#e8ecf5;border-radius:2px}
.fbw .people{position:absolute;left:6px;top:55px;display:flex;gap:18px}
.fbw .people div{width:30px;text-align:center;font-size:5.5px;color:#777}
.fbw .people i{display:block;width:30px;height:30px;background:#c9b8a4;margin-bottom:2px}

.loc{left:499px;top:736px;width:195px;height:146px;border:1px solid var(--line)}
.loc .hd{height:24px;background:linear-gradient(#7a5a0c,#5b4206);color:#fff;font-family:"PT Sans",sans-serif;font-weight:700;font-size:13px;padding:3px 5px}
.loc .map{position:absolute;left:2px;top:26px;width:189px;height:116px;background:linear-gradient(135deg,#e9e5dc,#dcd7cc)}

.band{left:0;top:898px;width:779px;height:156px;background:var(--paper-dark)}
.rule{top:912px;height:3px;border-top:1px solid var(--red);border-bottom:1px solid var(--red)}
.stats-title{left:0;width:779px;top:904px;text-align:center;font-family:"PT Sans",sans-serif;font-weight:700;font-size:14px;color:var(--red-dark)}
.stat{top:928px;width:189px;height:104px;background:#f3dfa4}
.stat .hd{height:24px;background:var(--red);color:#fff;font-family:"PT Sans",sans-serif;font-weight:700;font-size:13px;padding:3px 7px;position:relative}
.stat .hd::after{content:"";position:absolute;right:6px;top:5px;width:14px;height:14px;border-radius:50%;background:#e46b3e}
.stat .cols{display:flex;height:16px;background:var(--red-light);color:#fff;font-family:"PT Sans",sans-serif;font-weight:700;font-size:10.5px;line-height:16px}
.stat .row{display:flex;height:21px;line-height:21px;font-size:8px;font-weight:700;border-bottom:1px solid #fff6dc}
.c1{width:34px;padding-left:7px}.c2{width:92px;color:var(--red)}.c3{flex:1}
.stat .cols .c2{color:#fff;text-align:center}

.partners-tab{left:326px;top:1054px;width:126px;height:22px;background:var(--olive);clip-path:polygon(0 0,100% 0,88% 100%,12% 100%);color:#fff;font-family:"PT Sans",sans-serif;font-weight:700;font-size:12.5px;text-align:center;line-height:22px}
.partner{top:1096px;font-family:"PT Sans",sans-serif;font-weight:700;font-size:16px;color:#555}
.chev{top:1097px;width:10px;height:14px;background:var(--red)}

.footer{left:0;top:1140px;width:779px;height:60px;background:linear-gradient(#c24a22,#a93914)}
.footer .name{position:absolute;left:88px;top:14px;width:50px;text-align:center;font-family:"PT Sans",sans-serif;font-weight:700;font-size:9px;line-height:1.05;color:var(--yellow)}
.footer .links{position:absolute;right:86px;top:16px;font-size:7.5px;font-weight:700;color:#fff}
.footer .copy{position:absolute;left:354px;top:38px;font-size:7px;color:#fbe2d3}
</style>
</head>
<body>

<div class="abs brand"><div class="dot"></div><span>Redline Throw Club</span></div>

<div class="abs results"></div>
<div class="abs results-tab">RESULTS</div>
<div class="abs match" style="left:225px"><b>WEEKLY MATCHES</b><small>20.10.2013 - 18:30</small><i class="a"></i><div class="teams">Team - 1<br>vs<br>Team - 2</div><i class="b"></i></div>
<div class="abs match" style="left:343px"><b>WEEKLY MATCHES</b><small>20.10.2013 - 18:30</small><i class="a"></i><div class="teams">Team - 1<br>vs<br>Team - 2</div><i class="b"></i></div>
<div class="abs match" style="left:461px"><b>WEEKLY MATCHES</b><small>20.10.2013 - 18:30</small><i class="a"></i><div class="teams">Team - 1<br>vs<br>Team - 2</div><i class="b"></i></div>
<div class="abs match" style="left:579px"><b>WEEKLY MATCHES</b><small>20.10.2013 - 18:30</small><i class="a"></i><div class="teams">Team - 1<br>vs<br>Team - 2</div><i class="b"></i></div>
<div class="abs next">Next »</div>

<nav class="abs nav"><ul>
<li class="on" style="width:57px">Home</li><li style="width:69px">About</li><li style="width:67px">Teams</li><li style="width:79px">Schedule</li><li style="width:63px">News</li><li style="width:100px">Photos And Videos</li><li style="width:75px">Register</li><li style="width:98px;border:0">Contact Us</li>
</ul></nav>

<div class="abs hero" role="img" aria-label="Dodgeball players lunging on an indoor blue court"></div>
<div class="abs hero-cap"><h1>SO YOU THINK YOU CAN DODGE?</h1><div class="dots"><i class="on"></i><i></i><i></i><i></i></div></div>

<section class="abs panel news">
<h2>Latest News</h2>
<div class="photo" role="img" aria-label="Player throwing a dodgeball"></div>
<div class="lead"><b>Lorem ipsum dolor sit amet.</b><em>[ 29-10-2013 ]</em>Lorem ipsum dolor sit amet, inth consecte adipsi sed diam ameti nonummy nibh euism in tincidunt utopi laoree dolore magna inova aliquam erat volutpat. Utioa wisi enim ad minimamio veniam, quis</div>
<ul>
<li>29-10-2013<span>Lorem ipsum dolor sit amet .</span></li>
<li>29-10-2013<span>Lorem ipsum dolor sit amet .</span></li>
<li>29-10-2013<span>Lorem ipsum dolor sit amet .</span></li>
<li>29-10-2013<span>Lorem ipsum dolor sit amet .</span></li>
<li>29-10-2013<span>Lorem ipsum dolor sit amet .</span></li>
</ul>
</section>

<div class="abs like"><p style="top:2px;font-size:21px">Like us on</p><p style="top:32px;font-size:21px;font-weight:700">Friendstream</p><div class="sq"></div></div>
<div class="abs panel register"><h3>OPEN REGISTER HERE</h3><p>Lorem ipsum dolor sit amet,</p><div class="btn">REGISTER NOW</div><div class="mini">Redline Throw Club</div></div>

<section class="abs panel standing">
<h2>Season 1 Standing</h2>
<div class="tabs"><div class="on">Ultimate Rubber league</div><div>Ultimate Foam league</div></div>
<div class="table-wrap"><table>
<tr><th class="c" style="width:44px">Rank</th><th>Team Name</th><th style="width:70px">Score</th><th style="width:66px"></th></tr>
<tr><td class="c">1</td><td>Lorem ipsum dolor sit</td><td>8100</td><td class="c">1<i class="up"></i><i class="dn"></i></td></tr>
<tr><td class="c">2</td><td>Lorem ipsum dolor sit</td><td>8100</td><td class="c">2<i class="up"></i><i class="dn"></i></td></tr>
<tr><td class="c">3</td><td>Lorem ipsum dolor sit</td><td>8100</td><td class="c">3<i class="up"></i><i class="dn"></i></td></tr>
<tr><td class="c">4</td><td>Lorem ipsum dolor sit</td><td>8100</td><td class="c">4<i class="up"></i><i class="dn"></i></td></tr>
<tr><td class="c">5</td><td>Lorem ipsum dolor sit</td><td>8100</td><td class="c">5<i class="up"></i><i class="dn"></i></td></tr>
<tr><td class="c">6</td><td>Lorem ipsum dolor sit</td><td>8100</td><td class="c">6<i class="up"></i><i class="dn"></i></td></tr>
<tr><td class="c">7</td><td>Lorem ipsum dolor sit</td><td>8100</td><td class="c">7<i class="up"></i><i class="dn"></i></td></tr>
<tr><td class="c">8</td><td>Lorem ipsum dolor sit</td><td>8100</td><td class="c">8<i class="up"></i><i class="dn"></i></td></tr>
<tr><td class="c">9</td><td>Lorem ipsum dolor sit</td><td>8100</td><td class="c">9<i class="up"></i><i class="dn"></i></td></tr>
<tr><td class="c">10</td><td>Lorem ipsum dolor sit</td><td>8100</td><td class="c">10<i class="up"></i><i class="dn"></i></td></tr>
</table></div>
</section>

<aside class="abs fbw">
<div class="hd">Friendstream</div>
<i class="arr" style="right:21px"></i><i class="arr" style="right:7px"></i>
<div class="abs" style="left:7px;top:30px;width:22px;height:20px;background:#f0c060"></div>
<div class="abs" style="left:90px;top:37px;font-size:5.5px;color:#3b5998">Like &nbsp; 108 people like this page</div>
<div class="people"><div><i></i>Mira</div><div><i></i>Ravi</div><div><i></i>Mira</div><div><i></i>Ravi</div></div>
<div class="abs" style="left:8px;top:107px;font-size:5.5px;color:#777">Friendstream social plugin</div>
<div class="abs" style="right:6px;top:105px;font-size:8px;font-weight:700;color:#3b5998">Join Us!</div>
</aside>

<aside class="abs loc"><div class="hd">Location</div><div class="map" role="img" aria-label="Street map showing the league venue"></div></aside>

<div class="abs band"></div>
<div class="abs rule" style="left:86px;width:254px"></div>
<div class="abs rule" style="left:440px;width:254px"></div>
<div class="abs stats-title">League Stats</div>

<div class="abs stat" style="left:86px"><div class="hd">Top 3 Killer</div><div class="cols"><span class="c1">#</span><span class="c2">Name</span><span class="c3" style="text-align:center">Team</span></div>
<div class="row"><span class="c1">1</span><span class="c2">Utioa Wisi Enim</span><span class="c3">Minimamio</span></div><div class="row"><span class="c1">2</span><span class="c2">Utioa Wisi Enim</span><span class="c3">Minimamio</span></div><div class="row"><span class="c1">3</span><span class="c2">Utioa Wisi Enim</span><span class="c3">Minimamio</span></div></div>
<div class="abs stat" style="left:295px"><div class="hd">Top 3 Catcher</div><div class="cols"><span class="c1">#</span><span class="c2">Name</span><span class="c3" style="text-align:center">Team</span></div>
<div class="row"><span class="c1">1</span><span class="c2">Utioa Wisi Enim</span><span class="c3">Minimamio</span></div><div class="row"><span class="c1">2</span><span class="c2">Utioa Wisi Enim</span><span class="c3">Minimamio</span></div><div class="row"><span class="c1">3</span><span class="c2">Utioa Wisi Enim</span><span class="c3">Minimamio</span></div></div>
<div class="abs stat" style="left:505px"><div class="hd">Top 3 Dodger</div><div class="cols"><span class="c1">#</span><span class="c2">Name</span><span class="c3" style="text-align:center">Team</span></div>
<div class="row"><span class="c1">1</span><span class="c2">Utioa Wisi Enim</span><span class="c3">Minimamio</span></div><div class="row"><span class="c1">2</span><span class="c2">Utioa Wisi Enim</span><span class="c3">Minimamio</span></div><div class="row"><span class="c1">3</span><span class="c2">Utioa Wisi Enim</span><span class="c3">Minimamio</span></div></div>

<div class="abs partners-tab">Our Partners</div>
<div class="abs chev" style="left:86px;clip-path:polygon(100% 0,0 50%,100% 100%)"></div>
<div class="abs partner" style="left:118px">Brightmoor</div>
<div class="abs partner" style="left:253px;color:#c92020">Tellaris</div>
<div class="abs partner" style="left:356px">Quantex</div>
<div class="abs partner" style="left:476px">Vertex Tech</div>
<div class="abs partner" style="left:574px;color:#1f6fb0">Ledgerly</div>
<div class="abs chev" style="left:685px;clip-path:polygon(0 0,100% 50%,0 100%)"></div>

<footer class="abs footer">
<div class="name">Redline Throw Club</div>
<div class="links">Home &nbsp;| &nbsp;About &nbsp;| &nbsp;Teams &nbsp;| &nbsp;Schedule &nbsp;| &nbsp;News &nbsp;| &nbsp;Photos and Videos &nbsp;| &nbsp;Register &nbsp;| &nbsp;Contact Us</div>
<div class="copy">Copyright © 2013 redlinethrowclub.org. All rights reserved.</div>
</footer>

</body>
</html>
```